Customer Value Leaflet

We need a bi-fold brochure designing, based on the attached PDF wireframes. Our company name is quillbrookery.com (of which the logo is currently being designed). The corporate colour is orange (the exact shade of which we are happy to leave to the designers discretion).

The leaflet will distributed to customer experience experts and marketers so the design needs to be bright, engaging, clean and simple. Design is critical.

```html
<!DOCTYPE html>
<html lang="en">
<head>
<meta charset="utf-8">
<title>quillbrookery.com – Customer Value Leaflet</title>
<link rel="stylesheet" href="https://fonts.googleapis.com/css2?family=Amatic+SC:wght@400;700&family=Raleway:wght@400;600&display=swap">
<style>
  :root {
    --stage: #e4e4e4;
    --paper: #fbfbfb;
    --orange: #ef7d35;
    --orange-soft: #fde3d2;
    --peach: #f4a07a;
    --blue: #2f92c7;
    --blue-soft: #dce9f4;
    --sky: #7fc0de;
    --ink: #1e1e1e;
    --grey: #555555;
  }
  * { box-sizing: border-box; margin: 0; padding: 0; }
  html, body { width: 1200px; height: 800px; overflow: hidden; }
  body {
    background: var(--stage);
    font-family: "Raleway", "Century Gothic", sans-serif;
    display: flex; align-items: center; justify-content: center;
  }
  .spread { display: flex; width: 1000px; height: 660px; box-shadow: 0 10px 30px rgba(0,0,0,.18); }
  .panel { position: relative; width: 500px; height: 660px; background: var(--paper); overflow: hidden; }
  .panel--inside { border-right: 1px solid #e2e2e2; }

  /* inside panel */
  .intro-blob {
    position: absolute; left: 30px; top: 40px; width: 330px; height: 140px;
    background: var(--orange-soft); border-radius: 70px 80px 90px 60px / 60px 70px 80px 70px;
  }
  .intro-text {
    position: absolute; left: 58px; top: 58px; width: 290px;
    color: var(--orange); font-size: 21px; line-height: 1.2;
  }
  .benefit-blob {
    position: absolute; left: 20px; top: 210px; width: 440px; height: 400px;
    background: var(--blue-soft); border-radius: 120px 90px 110px 100px / 100px 120px 90px 110px;
  }
  .illustration {
    position: absolute; left: 50px; top: 200px; width: 380px; height: 170px;
    border-radius: 16px;
    background: linear-gradient(135deg, #c9dcec 0%, #f3f3f3 55%, #f7c7a6 100%);
  }
  .benefit-text {
    position: absolute; left: 56px; top: 392px; width: 390px;
    color: var(--blue); font-size: 22px; line-height: 1.25;
  }
  .brand, .em { font-weight: 600; }
  .intro-text .brand { color: var(--orange); }

  /* cover panel */
  .name-tab {
    position: absolute; left: 110px; top: 0; width: 290px; height: 100px;
    background: var(--orange); border-radius: 0 0 60px 60px;
    display: flex; align-items: center; justify-content: center;
    color: #ffffff; font-weight: 600; font-size: 24px;
  }
  .tagline-lead { position: absolute; left: 70px; top: 140px; font-size: 26px; color: var(--ink); }
  .word-blob {
    position: absolute; display: flex; align-items: center; justify-content: center;
    font-family: "Amatic SC", "Comic Sans MS", cursive; font-weight: 400; color: #ffffff;
    letter-spacing: 4px;
  }
  .word-blob--customer {
    left: 60px; top: 180px; width: 420px; height: 180px;
    background: var(--sky); border-radius: 50%; transform: rotate(-8deg);
    font-size: 110px;
  }
  .word-blob--value {
    left: 150px; top: 310px; width: 330px; height: 190px;
    background: var(--peach); opacity: .9; border-radius: 45%; transform: rotate(-4deg);
    font-size: 120px;
  }
  .tagline-end { position: absolute; left: 300px; top: 505px; font-size: 28px; color: var(--grey); }
</style>
</head>
<body>
  <main class="spread">
    <section class="panel panel--inside">
      <div class="intro-blob"></div>
      <p class="intro-text"><span class="brand">VANTIRO</span> is our Customer Value Platform, designed for Marketers in the Digital Enterprise.</p>
      <div class="benefit-blob"></div>
      <div class="illustration" role="img" aria-label="Illustration of a rising line chart, magnifying glass, browser window and test tubes in orange and blue"></div>
      <p class="benefit-text"><span class="brand">VANTIRO</span> is like having a team of <span class="em">data scientists</span> making valuable insights available to your website in real-time so that you can deliver <span class="em">the ultimate customer experience</span></p>
    </section>
    <section class="panel panel--cover">
      <div class="name-tab">quillbrookery.com</div>
      <p class="tagline-lead">We’re a</p>
      <div class="word-blob word-blob--customer">CUSTOMER</div>
      <div class="word-blob word-blob--value">VALUE</div>
      <p class="tagline-end">Company</p>
    </section>
  </main>
</body>
</html>
```